New Tequila Alcohol Package Design

We are launching a new premium pre-made tequila jello shot product. We currently have a vodka jello 20 pack product. Please see our website and Instagram for current product:
https://zingcubes.com/
https://www.instagram.com/zingcubes/
PROJECT DETAILS:
Design a 4 pack jello shot box. Box similar to: https://buyspiritsqrd.ca/products/curly-dropz-lucky-fox-4-x-30-ml
there will be one main image (top) and a front and back side (small). Please see the dimensions.
PLEASE SEE DESIGN TEMPLATE.
Dimensions are: 12.5cm*12.5cm*1.5cm
LOGO: ZINGcubes Agave Gelatin Shots
FLAVOUR: Margarita Raspberry
DESIGN: We don't have a lot of directions for this. We are potentially looking for something completely different than what we already have, so please keep that in mind.
OUR BRAND: Fun, bold, colorful, outrageous. Needs to be eye-catching to be grabbed off of the shelf in a crowded liquor industry.
ZING - it's gone. Reasoning for the brand. The brand is a bit of a "joke" and is not serious.
We have used fruit "emoji/vectors" in the background in the past.

We will require more than one design in the future (we already have more than one flavour ready to market). We are looking for a designer we can potentially work with on future projects.

Target Market(s)

18-29, more female/GenZ-focused.

Industry/Entity Type

alcohol

Font styles to use
Other font styles liked:
• Please choose for us. Ideally "MARGARITA" is the main focus.

Requirements
Must have
• Please see the Text Required Document

```html
<!DOCTYPE html>
<html lang="en">
<head>
<meta charset="utf-8">
<title>ZINGcubes Margarita Raspberry – 4 pack box dieline</title>
<link rel="stylesheet" href="https://fonts.googleapis.com/css2?family=Luckiest+Guy&family=Oswald:wght@500;700&family=Roboto+Condensed:wght@400&display=swap">
<style>
  :root {
    --ink: #000000;
    --berry-red: #e31c4b;
    --berry-pink: #ff4378;
    --berry-deep: #e01a4a;
    --hex-line: #a8203f;
    --flavour-pink: #ee3a79;
    --tag-orange: #f28c1c;
    --sun-yellow: #fff200;
    --paper: #ffffff;
    --logo-ink: #141414;
  }
  * { margin: 0; padding: 0; box-sizing: border-box; }
  html, body { width: 1200px; height: 579px; overflow: hidden; background: var(--ink); }
  .canvas { position: relative; width: 1200px; height: 579px; background: var(--ink); }
  .panel { position: absolute; top: 73.6px; height: 431px; }

  .glue-flap { left: 87.6px; width: 56.8px; background: var(--berry-red); }

  .back-panel { left: 144.4px; width: 431px; background: var(--berry-pink); overflow: hidden; }
  .back-art { position: absolute; left: 6px; top: -10px; width: 370px; height: 450px;
    background: radial-gradient(ellipse at 50% 55%, var(--berry-deep) 0 58%, transparent 60%); }
  .tray-guides { position: absolute; inset: 0; }

  .info-panel { left: 575.3px; width: 55.9px; background: var(--berry-red); color: var(--paper);
    font-family: "Roboto Condensed", sans-serif; }
  .info-text { position: absolute; writing-mode: vertical-rl; text-transform: uppercase; }
  .ingredients { right: 5px; top: 8px; height: 200px; font-size: 7px; line-height: 9px; }
  .importer-rule { position: absolute; left: 6px; right: 5px; top: 214px; border-top: 0.7px solid var(--paper); }
  .importer { right: 12px; top: 220px; height: 140px; font-size: 6px; line-height: 7.5px; }
  .lot-box { position: absolute; left: 6px; top: 376px; width: 43px; height: 53px; background: var(--paper); }

  .front-panel { left: 631.2px; width: 430.8px; overflow: hidden;
    background: linear-gradient(135deg, #cfeef3 0%, #fff7b8 30%, #ffd3e2 55%, #d5dcf3 80%, #cfeef3 100%); }
  .front-pattern { position: absolute; inset: 0; }

  .strength-badge { position: absolute; left: 270px; top: 13px; width: 143px; height: 54px;
    background: var(--berry-red); color: var(--sun-yellow); text-align: center;
    font-family: "Luckiest Guy", sans-serif; }
  .strength-badge .abv { display: block; font-size: 14px; margin-top: 6px; letter-spacing: .5px; }
  .strength-badge .volume { display: block; font-size: 24px; line-height: 1; letter-spacing: 1px; }

  .brand-name { position: absolute; left: 30px; top: 82px; width: 370px; text-align: center;
    font-family: "Luckiest Guy", sans-serif; color: var(--logo-ink); line-height: .9; }
  .brand-name .main { display: block; font-size: 118px; }
  .brand-name .sub { display: block; font-size: 66px; margin-left: 140px; margin-top: 6px; }

  .claim-tags { position: absolute; left: 48px; top: 216px; font-family: "Oswald", sans-serif;
    font-weight: 700; font-size: 18px; color: var(--ink); transform: rotate(-3deg); }
  .claim-tags span { display: block; width: fit-content; background: var(--tag-orange);
    padding: 0 6px; line-height: 27px; margin-bottom: 4px; }
  .claim-tags .agave { margin-left: 18px; }
  .claim-tags .gelatin { margin-left: 2px; }

  .flavour-badge { position: absolute; left: 110px; top: 324px; width: 207px; height: 80px;
    background: var(--flavour-pink); display: flex; align-items: center; gap: 10px; padding-left: 18px; }
  .flavour-icon { width: 42px; height: 50px; border-radius: 50%; background: var(--sun-yellow); flex: none; }
  .flavour-name { font-family: "Oswald", sans-serif; font-weight: 700; color: var(--paper);
    font-size: 22px; line-height: 1.1; letter-spacing: .5px; }

  .side-panel { left: 1062px; width: 46.7px; background: var(--berry-red); color: var(--paper); }
  .side-brand { position: absolute; left: 50%; font-family: "Luckiest Guy", sans-serif; font-size: 16px;
    white-space: nowrap; color: var(--paper); transform: translate(-50%, -50%) rotate(90deg); }
  .side-brand.top { top: 48px; }
  .side-brand.bottom { top: 395px; }
  .side-flavour { position: absolute; left: 50%; top: 208px; transform: translate(-50%, -50%) rotate(90deg);
    font-family: "Oswald", sans-serif; font-weight: 700; font-size: 15px; line-height: 1.05;
    white-space: nowrap; text-align: center; }
</style>
</head>
<body>
<main class="canvas">
  <section class="panel glue-flap" role="img" aria-label="White brush dash pattern on raspberry red"></section>

  <section class="panel back-panel">
    <div class="back-art" role="img" aria-label="Large raspberry illustration in deep pink"></div>
    <svg class="tray-guides" viewBox="0 0 431 431" aria-hidden="true">
      <g fill="none" stroke="var(--hex-line)" stroke-width="1.2">
        <polygon points="52,114 82,61 143,61 173,114 143,167 82,167"/>
        <polygon points="254,114 284,61 345,61 375,114 345,167 284,167"/>
        <polygon points="52,321 82,268 143,268 173,321 143,374 82,374"/>
        <polygon points="254,321 284,268 345,268 375,321 345,374 284,374"/>
      </g>
    </svg>
  </section>

  <section class="panel info-panel">
    <p class="info-text ingredients">Ingredients: water, sugar, fructose, agave spirits, carrageenan, citric acid, malic acid, artificial flavor, allura red AC<br>Ingrédients: eau, sucre, fructose, esprits d'agave carraghénane, acide citrique, acide malique, saveur artificielle, rouge allura AC</p>
    <div class="importer-rule"></div>
    <p class="info-text importer">Imported by / Importé par:<br>Merry Batch Inc. Brookfell, AB.<br>Product of China / Produit de Chine.<br>Drink responsibly / Boire avec modération.</p>
    <div class="lot-box"></div>
  </section>

  <section class="panel front-panel">
    <div class="front-pattern" role="img" aria-label="Bold zigzag line pattern in cyan, yellow, pink and blue"></div>
    <div class="strength-badge"><span class="abv">12% ALC./VOL.</span><span class="volume">4X 50ML</span></div>
    <h1 class="brand-name"><span class="main">ZING</span><span class="sub">cubes</span></h1>
    <p class="claim-tags"><span class="premium">PREMIUM</span><span class="agave">AGAVE</span><span class="gelatin">GELATIN</span></p>
    <div class="flavour-badge">
      <div class="flavour-icon" role="img" aria-label="Yellow raspberry icon"></div>
      <p class="flavour-name">MARGARITA<br>RASPBERRY</p>
    </div>
  </section>

  <section class="panel side-panel" role="group" aria-label="Side panel">
    <p class="side-brand top">ZINGcubes</p>
    <p class="side-flavour">MARGARITA<br>RASPBERRY</p>
    <p class="side-brand bottom">ZINGcubes</p>
  </section>
</main>
</body>
</html>
```